Corporate Business Card

Very professional, Modern, Not to busy, include phone address email, website
(253) 555-0174, 61807 19th Street N, Kent, WA 98517, marcus@kestrelbayholding.com, brelvanindustries.com

Target Market(s)

Manufacturing

Industry/Entity Type

Aero, machining, manufacturing, Off road racing

Contact Information for Business Card

Phone, address email, website

```html
<!DOCTYPE html>
<html lang="en">
<head>
<meta charset="utf-8">
<title>Brelvan Industries – Business Card</title>
<link href="https://fonts.googleapis.com/css2?family=Montserrat:wght@300;400;600;700&display=swap" rel="stylesheet">
<style>
  :root {
    --backdrop: #1e1f22;
    --card-navy: #17346e;
    --accent-red: #d6222c;
    --ink-white: #ffffff;
    --ink-soft: #dfe5f2;
  }
  * { margin: 0; padding: 0; box-sizing: border-box; }
  html, body {
    width: 1200px; height: 817px; overflow: hidden;
    background: var(--backdrop);
    font-family: "Montserrat", Arial, sans-serif;
  }
  .canvas { position: relative; width: 1200px; height: 817px; }
  .card {
    position: absolute;
    width: 540px; height: 308px;
    background: var(--card-navy);
    border-radius: 24px;
    overflow: hidden;
  }
  .card--front { left: 50px; top: 90px; }
  .card--back { left: 620px; top: 420px; }

  .brand { position: absolute; }
  .brand__name {
    display: flex; align-items: center; gap: 12px;
    color: var(--ink-white);
    font-weight: 700;
    letter-spacing: 0.5px;
    white-space: nowrap;
  }
  .brand__mark { width: 14px; height: 14px; background: var(--accent-red); flex: none; }
  .brand__rule { height: 1.5px; background: var(--ink-white); margin-top: 10px; }

  .card--front .brand { left: 0; right: 0; top: 122px; display: flex; flex-direction: column; align-items: center; }
  .card--front .brand__name { font-size: 32px; }
  .card--front .brand__rule { width: 200px; align-self: center; transform: translateX(-60px); }

  .card--back .brand { left: 36px; top: 100px; }
  .card--back .brand__name { font-size: 21px; gap: 10px; }
  .card--back .brand__mark { width: 10px; height: 10px; }
  .card--back .brand__rule { width: 130px; margin-top: 8px; }

  .person { position: absolute; right: 36px; top: 36px; text-align: right; }
  .person__name { font-size: 20px; color: var(--ink-white); font-weight: 300; letter-spacing: 1px; white-space: nowrap; }
  .person__surname { color: var(--accent-red); font-weight: 700; }
  .person__role { font-size: 12px; color: var(--ink-soft); font-weight: 400; margin-top: 4px; letter-spacing: 0.5px; }

  .contact {
    position: absolute; left: 36px; bottom: 30px;
    list-style: none; color: var(--ink-white);
    font-size: 12px; font-weight: 400; line-height: 1.6;
  }
  .contact__address { margin-bottom: 6px; }
  .contact__item { display: flex; align-items: center; gap: 10px; }
  .contact__icon { width: 12px; height: 12px; flex: none; }
</style>
</head>
<body>
<main class="canvas">
  <section class="card card--front" aria-label="Card front">
    <div class="brand">
      <div class="brand__name"><span class="brand__mark"></span>Brelvan Industries</div>
      <div class="brand__rule"></div>
    </div>
  </section>

  <section class="card card--back" aria-label="Card back">
    <div class="person">
      <div class="person__name">DARA <span class="person__surname">WHITFIELD</span></div>
      <div class="person__role">Director / CEO</div>
    </div>

    <div class="brand">
      <div class="brand__name"><span class="brand__mark"></span>Brelvan Industries</div>
      <div class="brand__rule"></div>
    </div>

    <ul class="contact">
      <li class="contact__address">61807 19th Street N, Kent,<br>WA 98517</li>
      <li class="contact__item">
        <svg class="contact__icon" viewBox="0 0 24 24" aria-hidden="true"><path fill="#d6222c" d="M6.6 10.8a15 15 0 0 0 6.6 6.6l2.2-2.2c.3-.3.7-.4 1-.2 1.1.4 2.3.6 3.6.6.6 0 1 .4 1 1V20c0 .6-.4 1-1 1A17 17 0 0 1 3 4c0-.6.4-1 1-1h3.5c.6 0 1 .4 1 1 0 1.3.2 2.5.6 3.6.1.3 0 .7-.2 1z"/></svg>
        (253) 555-0174
      </li>
      <li class="contact__item">
        <svg class="contact__icon" viewBox="0 0 24 24" aria-hidden="true"><rect x="2" y="5" width="20" height="14" rx="1" fill="#d6222c"/><path d="M2 6l10 7 10-7" fill="none" stroke="#17346e" stroke-width="1.8"/></svg>
        marcus@kestrelbayholding.com
      </li>
      <li class="contact__item">
        <svg class="contact__icon" viewBox="0 0 24 24" aria-hidden="true"><circle cx="12" cy="12" r="10" fill="#d6222c"/><path d="M2 12h20M12 2c3 3 3 17 0 20M12 2c-3 3-3 17 0 20" fill="none" stroke="#17346e" stroke-width="1.5"/></svg>
        brelvanindustries.com
      </li>
    </ul>
  </section>
</main>
</body>
</html>
```